Boracay Wedding Invitation Design

Hello, We would like a wedding invitation design for our wedding in Boracay. We would like it somewhat in the form of a boarding pass with beachy fresh colours, possibly a nice Boracay beach in the background Double sided with an envelope design to match. Maybe something simple on the envelope like a nice picture in the bottom left corner of a shell on a beach or something similar.

I would also like on the opposite side of the invite to be an "information sheet" with a matching beach design

The text files for both sides are included and i have also included 2 designs that i thought looked nice and are similar to what we are after.
Updates

Hello, I have updated the brief to be more specific with text files and images to make it easier for you. Thank you :)

Industry/Entity Type

Wedding

Font styles to use
Decorative
Script

Colors
fbee3d
33a6d7
33b8a4
fbf289
85cae6
ffffff

Requirements
Must have
• I would like to have this quote somewhere on the invitation
• This day I will marry my best friend,
• the one I laugh with,
• live for,
• dream with,
• love
• Owen & Marisa
• Request the pleasure of your company to celebrate their wedding
• On Friday the 17th March 2017
• at
• Velunda Grand Suites
• Boracay, Philippines
• Ceremony begins at 3.00pm
• RSVP
• Owen 0431907254
• Marisa 0417283649
• by
• 17th Jan 2016
• Dress: Beach Formal
• For the "information sheet"
• There will be a 5% discount on rooms booked at the Velunda under the event Owen & Marisa Wedding. The resort has a total of 24 rooms it would be nice if the majority of guests could stay at the resort from the night before until the night after the wedding but if you choose to stay elsewhere on the island there are plenty of other places to stay for cheaper and everything is fairly close as its a small island.
• We have currently blocked room stay for a short period of time so our guests can book rooms. If you choose to do so please email reservations@velundastays.example. Once rooms become available to the public again, towards the end of Jan, it will be first come first served basis. The resort is very popular so im assuming once this happens the rooms will be booked out.
• If you would like to check out the resort itself the website is www.velundagrand-isle.example
• We know its a fair distance to travel but we would really love to see you all there to celebrate and maybe even enjoy a small holiday while your here its a beautiful part of the world.
• If anyone has any questions please feel free to contact Owen on 0431907254
Nice to have
• A nice picture of a Boracay beach in the background would be nice

```html
<!DOCTYPE html>
<html lang="en">
<head>
<meta charset="utf-8">
<title>Owen &amp; Marisa – Wedding Boarding Pass</title>
<link rel="stylesheet" href="https://fonts.googleapis.com/css2?family=Great+Vibes&family=Poiret+One&family=Didact+Gothic&family=Montserrat:wght@600;800&display=swap">
<style>
  :root {
    --page-yellow: #fbf289;
    --ticket-white: #ffffff;
    --ocean-blue: #33a6d7;
    --sky-blue: #85cae6;
    --ink: #2b2b2b;
    --ink-soft: #4a4a4a;
    --edge: #c9d3dc;
  }
  * { margin: 0; padding: 0; box-sizing: border-box; }
  html, body { width: 1200px; height: 525px; overflow: hidden; background: var(--page-yellow); }
  .canvas { position: relative; width: 1200px; height: 525px; }

  .ticket {
    position: absolute; left: 10px; top: 14px; width: 1178px; height: 494px;
    background: var(--ticket-white); border: 1px solid var(--edge); border-radius: 6px;
  }
  .hero-photo {
    position: absolute; left: 283px; top: 15px; width: 776px; height: 492px;
    background:
      radial-gradient(ellipse 120px 170px at 78% 38%, rgba(244,190,160,0.95), rgba(244,190,160,0) 100%),
      radial-gradient(ellipse 190px 260px at 77% 50%, rgba(246,238,205,0.95), rgba(246,238,205,0) 100%),
      linear-gradient(180deg, #f1f4f8 0%, #d8e1ec 55%, #e9edf3 100%);
  }
  .ticket-edges { position: absolute; left: 0; top: 0; }

  .vertical { position: absolute; writing-mode: vertical-rl; white-space: nowrap; }

  /* stub (left) */
  .ceremony-time {
    left: 26px; top: 22px; height: 480px; text-align: center;
    font-family: "Poiret One", sans-serif; font-size: 29px; letter-spacing: 1px; color: var(--ink);
  }
  .rsvp-title { left: 180px; top: 26px; font-family: "Poiret One", sans-serif; font-size: 24px; color: var(--ocean-blue); letter-spacing: 1px; }
  .rsvp-line { font-family: "Poiret One", sans-serif; font-size: 15px; color: var(--ink-soft); letter-spacing: 0.5px; top: 26px; }
  .rsvp-owen { left: 206px; }
  .rsvp-marisa { left: 221px; }
  .rsvp-by { left: 236px; }
  .rsvp-dress { left: 251px; }

  .date-tag {
    position: absolute; left: 150px; top: 352px; width: 112px; height: 82px;
    background: var(--sky-blue); color: var(--ticket-white); text-align: center;
    font-family: "Montserrat", sans-serif; line-height: 1;
  }
  .date-tag .day { display: block; font-weight: 800; font-size: 26px; padding-top: 5px; }
  .date-tag .month { display: block; font-weight: 600; font-size: 11px; letter-spacing: 1px; margin-top: 3px; }
  .date-tag .year { display: block; font-weight: 800; font-size: 31px; margin-top: 2px; }
  .venue-caption {
    position: absolute; left: 150px; top: 438px; width: 112px; text-align: center;
    font-family: "Didact Gothic", sans-serif; font-size: 9px; line-height: 1.3; color: var(--ink-soft);
  }

  /* main panel */
  .couple-names {
    position: absolute; left: 364px; top: 34px;
    font-family: "Great Vibes", cursive; font-size: 66px; color: var(--ocean-blue); line-height: 1;
  }
  .invitation-line {
    position: absolute; left: 366px; top: 178px;
    font-family: "Didact Gothic", sans-serif; font-size: 17px; line-height: 1.35; color: var(--ink);
    text-transform: uppercase;
  }
  .quote {
    position: absolute; left: 330px; top: 288px; width: 620px; text-align: center;
    font-family: "Great Vibes", cursive; font-size: 30px; line-height: 1.45; color: var(--ocean-blue);
  }
  .wedding-date {
    position: absolute; left: 283px; top: 436px; width: 776px; text-align: center;
    font-family: "Poiret One", sans-serif; font-size: 35px; letter-spacing: 2px; color: var(--ink);
  }

  /* pass stub (right) */
  .pass-label { left: 1074px; top: 28px; font-family: "Poiret One", sans-serif; font-size: 26px; color: var(--ocean-blue); }
  .pass-label .script { font-family: "Great Vibes", cursive; font-size: 30px; color: var(--ink); }
  .pass-event { left: 1108px; top: 230px; font-family: "Poiret One", sans-serif; font-size: 36px; letter-spacing: 2px; color: var(--ink); }
  .pass-date { left: 1148px; top: 28px; font-family: "Poiret One", sans-serif; font-size: 25px; letter-spacing: 1px; color: var(--ocean-blue); }
</style>
</head>
<body>
<main class="canvas">
  <div class="ticket"></div>
  <div class="hero-photo" role="img" aria-label="Soft sky with clouds and a glass of rosé wine"></div>

  <svg class="ticket-edges" width="1200" height="525" viewBox="0 0 1200 525" aria-hidden="true">
    <g fill="var(--page-yellow)" stroke="var(--edge)" stroke-width="1">
      <circle cx="283" cy="14" r="11"/>
      <circle cx="283" cy="508" r="11"/>
      <circle cx="1060" cy="14" r="11"/>
      <circle cx="1060" cy="508" r="11"/>
    </g>
    <g stroke="var(--ocean-blue)" stroke-width="1.5" stroke-dasharray="4 4">
      <line x1="283" y1="27" x2="283" y2="495"/>
      <line x1="1060" y1="27" x2="1060" y2="495"/>
    </g>
  </svg>

  <section class="stub">
    <p class="vertical ceremony-time">CEREMONY BEGINS AT 3:00PM</p>
    <p class="vertical rsvp-title">RSVP</p>
    <p class="vertical rsvp-line rsvp-owen">OWEN: 0431907254</p>
    <p class="vertical rsvp-line rsvp-marisa">MARISA: 0417283649</p>
    <p class="vertical rsvp-line rsvp-by">BY 17TH JAN 2016</p>
    <p class="vertical rsvp-line rsvp-dress">DRESS: BEACH FORMAL</p>
    <div class="date-tag">
      <span class="day">FRIDAY</span>
      <span class="month">MARCH 17TH</span>
      <span class="year">2017</span>
    </div>
    <p class="venue-caption">Velunda Grand Suites<br>Boracay, Philippines</p>
  </section>

  <section class="invitation">
    <h1 class="couple-names">Owen &amp; Marisa</h1>
    <p class="invitation-line">Request the pleasure of your company<br>to celebrate their wedding</p>
    <p class="quote">This day I will marry my best friend, the one<br>I laugh with, live for, dream with, &amp; love</p>
    <p class="wedding-date">FRIDAY THE 17TH MARCH 2017</p>
  </section>

  <section class="pass">
    <p class="vertical pass-label">PASS: <span class="script">Owen &amp; Marisa</span></p>
    <p class="vertical pass-event">WEDDING</p>
    <p class="vertical pass-date">FRIDAY, MARCH 17TH 2017</p>
  </section>
</main>
</body>
</html>
```